Brightfold Systems, a software development company, needs a website

We need a website to promote our software development company. The company is brand new and we want to market ourselves. We develop all kinds of software from web applications, to desktop applications, to mobile applications. Small company, not a lot of history, just need something flashy.

```html
<!DOCTYPE html>
<html lang="en">
<head>
<meta charset="utf-8">
<title>Brightfold Systems — Software Development</title>
<link href="https://fonts.googleapis.com/css2?family=Montserrat:wght@400;500;600;700&family=Open+Sans:wght@400;600&display=swap" rel="stylesheet">
<style>
:root{
  --gold:#e6b70a;
  --gold-dark:#c9a010;
  --ink:#1d1d1d;
  --charcoal:#3a3a3a;
  --muted:#9a9a9a;
  --band:#f0f0f0;
  --teal:#1aa3b8;
  --white:#ffffff;
}
*{margin:0;padding:0;box-sizing:border-box}
html,body{width:1200px;height:3585px;overflow:hidden}
body{position:relative;background:var(--white);font-family:"Open Sans",Arial,sans-serif;color:var(--ink)}
.abs{position:absolute}

/* header + hero */
.hero{left:0;top:0;width:1200px;height:579px;background:linear-gradient(110deg,#2a2d30 0%,#4b5158 45%,#7c858c 75%,#5c6166 100%)}
.hero-shade{left:0;top:0;width:1200px;height:579px;background:linear-gradient(90deg,rgba(0,0,0,.45),rgba(0,0,0,0) 70%)}
.topbar{left:0;top:0;width:1200px;height:84px;background:rgba(196,163,32,.88)}
.brand{left:112px;top:22px;display:flex;align-items:center;gap:10px;color:var(--white);font-family:"Montserrat",sans-serif;font-weight:600;font-size:23px;line-height:1}
.brand-dot{width:30px;height:30px;background:var(--white)}
.nav{right:112px;top:34px;display:flex;gap:25px;font-family:"Montserrat",sans-serif;font-weight:600;font-size:14px;color:var(--white)}
.hero-title{left:112px;top:232px;font-family:"Montserrat",sans-serif;font-weight:700;font-size:45px;color:var(--white)}
.hero-sub{left:112px;top:302px;font-family:"Montserrat",sans-serif;font-size:22px;color:var(--white)}
.btn-read{left:112px;top:355px;width:120px;height:44px;border-radius:22px;background:var(--gold);color:var(--white);font-family:"Montserrat",sans-serif;font-weight:600;font-size:15px;display:flex;align-items:center;justify-content:center}
.dots{left:552px;top:541px;display:flex;gap:8px}
.dots span{width:13px;height:13px;border-radius:50%;background:rgba(255,255,255,.55)}
.dots span:first-child{background:var(--white)}
.notch{left:540px;width:120px;height:62px}

/* develop */
.dev-brand{left:0;width:1200px;top:680px;text-align:center;font-family:"Montserrat",sans-serif;font-weight:700;font-size:20px;color:var(--ink)}
.dev-brand i{display:inline-block;width:14px;height:14px;background:var(--gold);margin-right:8px;vertical-align:middle}
.dev-kicker{left:0;width:1200px;top:758px;text-align:center;font-family:"Montserrat",sans-serif;font-weight:600;font-size:23px}
.dev-title{left:0;width:1200px;top:790px;text-align:center;font-family:"Montserrat",sans-serif;font-weight:700;font-size:32px;color:var(--gold);word-spacing:10px}
.devices{left:165px;top:995px;width:765px;height:330px;background:linear-gradient(120deg,#cfd3d6 0%,#5f7380 35%,#0e7f98 60%,#16335f 100%)}
.dev-label{font-family:"Montserrat",sans-serif;font-weight:600;font-size:18px;color:var(--ink)}

/* services */
.services{left:0;top:1506px;width:1200px;height:503px;background:var(--band)}
.sec-title{font-family:"Montserrat",sans-serif;font-weight:700;font-size:32px;color:var(--gold)}
.svc-rule{left:564px;top:1621px;width:72px;height:3px;background:var(--gold)}
.card{top:1690px;width:235px;height:228px;text-align:center;padding-top:24px;box-shadow:0 1px 4px rgba(0,0,0,.2)}
.card.light{background:var(--white);border-top:4px solid;border-image:linear-gradient(90deg,var(--gold),var(--charcoal)) 1}
.card.dark{background:linear-gradient(170deg,var(--gold) 0%,#a8891a 45%,#3e3d38 100%);color:var(--white)}
.card svg{display:block;margin:0 auto}
.card h3{font-family:"Montserrat",sans-serif;font-weight:600;font-size:17px;margin-top:22px}
.card.light h3{color:var(--gold)}
.card p{font-size:12.5px;line-height:20px;margin:6px 16px 0;color:#555}
.card.dark p{color:var(--white)}
.card .chev{margin-top:10px}

/* features */
.feat-pic{left:65px;top:2116px;width:468px;height:424px;background:linear-gradient(180deg,#f4f4f4 0%,#f0d45a 45%,#d9b514 70%,#3a4868 100%)}
.feat-base{left:65px;top:2540px;width:468px;height:2px;background:#ccc}
.feat{left:565px;width:524px}
.feat h2{font-family:"Montserrat",sans-serif;font-weight:700;font-size:32px;color:var(--gold)}
.feat h4{font-family:"Montserrat",sans-serif;font-weight:600;font-size:19px;color:var(--gold)}
.feat p{font-size:14px;line-height:22px;color:var(--muted)}

/* contact */
.contact{left:0;top:2645px;width:1200px;height:626px;background:linear-gradient(100deg,#2f2f2c 0%,#6b6247 35%,#c9a41a 70%,#e8b80a 100%)}
.contact-title{left:0;width:1200px;top:2724px;text-align:center;font-family:"Montserrat",sans-serif;font-weight:700;font-size:32px;color:var(--white)}
.contact-text{left:95px;width:1010px;top:2782px;text-align:center;font-size:15.5px;line-height:23px;color:var(--white)}
.field{left:320px;width:560px;border:2px solid var(--white);color:var(--white);font-size:15px;font-weight:600;padding:12px 14px}
.btn-submit{left:534px;top:3128px;width:133px;height:42px;border-radius:21px;background:var(--white);color:var(--gold);font-family:"Montserrat",sans-serif;font-size:15px;display:flex;align-items:center;justify-content:center}

/* footer */
.foot-brand{left:112px;top:3410px;display:flex;align-items:center;gap:10px;font-family:"Montserrat",sans-serif;font-weight:600;font-size:25px;color:var(--ink)}
.foot-brand i{width:30px;height:30px;background:var(--gold)}
.social{left:836px;top:3404px;display:flex;gap:10px}
.social span{width:42px;height:42px;border-radius:50%;border:2px solid #555}
.foot-rule{left:112px;top:3495px;width:976px;height:1px;background:#ccc}
.copyright{left:0;width:1200px;top:3537px;text-align:center;font-family:"Montserrat",sans-serif;font-size:14px;color:var(--ink)}
</style>
</head>
<body>

<!-- hero -->
<div class="abs hero" role="img" aria-label="Photo of a development team gathered around computer screens"></div>
<div class="abs hero-shade"></div>
<div class="abs topbar"></div>
<div class="abs brand"><span class="brand-dot"></span>Brightfold Systems</div>
<nav class="abs nav"><span>HOME</span><span>PORTFOLIO</span><span>SHOP</span><span>FEATURES</span><span>WORKS</span><span>BLOG</span><span>CONTACT</span></nav>
<h1 class="abs hero-title">BRIGHTFOLD SYSTEMS</h1>
<p class="abs hero-sub">We are a software development company in Canada.</p>
<div class="abs btn-read">Read More</div>
<div class="abs dots"><span></span><span></span><span></span><span></span><span></span></div>
<svg class="abs notch" style="top:578px" viewBox="0 0 120 62"><path d="M0 0 H120 C85 2 64 20 60 62 C56 20 35 2 0 0Z" fill="#5a5f64"/></svg>

<!-- we develop -->
<div class="abs dev-brand"><i></i>Brightfold Systems</div>
<div class="abs dev-kicker">WE DEVELOP</div>
<div class="abs dev-title">SOFTWARE APPLICATIONS</div>

<div class="abs devices" role="img" aria-label="Illustration of a laptop, desktop monitor and tablet showing software screens, with callouts for web, mobile and desktop applications"></div>
<div class="abs dev-label" style="left:146px;top:957px">WEB APPLICATIONS</div>
<div class="abs dev-label" style="left:874px;top:902px">MOBILE APPLICATIONS</div>
<div class="abs dev-label" style="left:653px;top:1389px">DESKTOP APPLICATIONS</div>

<!-- services -->
<section class="abs services"></section>
<h2 class="abs sec-title" style="left:0;width:1200px;top:1566px;text-align:center">OUR SERVICES</h2>
<div class="abs svc-rule"></div>

<div class="abs card light" style="left:110px">
  <svg width="56" height="44" viewBox="0 0 56 44" fill="none" stroke="#e6b70a" stroke-width="3"><rect x="6" y="10" width="32" height="22"/><path d="M2 36 H42"/><circle cx="42" cy="12" r="10" fill="#fff"/><path d="M36 12 c2-4 5 0 6 0 s4-4 6 0 s-4 4-6 0 s-4 4-6 0" stroke-width="2"/></svg>
  <h3>NEMO ENIM IPSAM</h3>
  <p>Excepteur sint occaecat cupidatat non proident, sunt in culpa qui officia deserunt mollit.</p>
  <svg class="chev" width="12" height="12" viewBox="0 0 12 12" fill="none" stroke="#e6b70a" stroke-width="1.6"><path d="M2 2 L6 6 L10 2 M2 6 L6 10 L10 6"/></svg>
</div>
<div class="abs card dark" style="left:358px">
  <svg width="44" height="44" viewBox="0 0 44 44" fill="none" stroke="#fff" stroke-width="2"><path d="M10 4 H30 L36 10 V40 H10Z"/><path d="M16 16 H30 M16 22 H30 M16 28 H30 M16 34 H26"/></svg>
  <h3>INVENTORE VERITATIS</h3>
  <p>Excepteur sint occaecat cupidatat non proident, sunt in culpa qui officia deserunt mollit.</p>
  <svg class="chev" width="12" height="12" viewBox="0 0 12 12" fill="none" stroke="#fff" stroke-width="1.6"><path d="M2 2 L6 6 L10 2 M2 6 L6 10 L10 6"/></svg>
</div>
<div class="abs card light" style="left:606px">
  <svg width="44" height="48" viewBox="0 0 44 48" fill="none" stroke="#e6b70a" stroke-width="2.5"><path d="M8 24 V18 a14 14 0 0 1 28 0 V24"/><rect x="5" y="22" width="7" height="12" rx="2"/><rect x="32" y="22" width="7" height="12" rx="2"/><circle cx="22" cy="24" r="7"/><path d="M12 46 a10 8 0 0 1 20 0"/></svg>
  <h3>NEMO ENIM IPSAM</h3>
  <p>Excepteur sint occaecat cupidatat non proident, sunt in culpa qui officia deserunt mollit.</p>
  <svg class="chev" width="12" height="12" viewBox="0 0 12 12" fill="none" stroke="#e6b70a" stroke-width="1.6"><path d="M2 2 L6 6 L10 2 M2 6 L6 10 L10 6"/></svg>
</div>
<div class="abs card dark" style="left:853px">
  <svg width="48" height="48" viewBox="0 0 48 48" fill="none" stroke="#fff" stroke-width="3"><circle cx="24" cy="24" r="13"/><circle cx="24" cy="24" r="5"/><path d="M24 3 V10 M24 38 V45 M3 24 H10 M38 24 H45 M9 9 L14 14 M34 34 L39 39 M39 9 L34 14 M14 34 L9 39"/></svg>
  <h3>INVENTORE VERITATIS</h3>
  <p>Excepteur sint occaecat cupidatat non proident, sunt in culpa qui officia deserunt mollit.</p>
  <svg class="chev" width="12" height="12" viewBox="0 0 12 12" fill="none" stroke="#fff" stroke-width="1.6"><path d="M2 2 L6 6 L10 2 M2 6 L6 10 L10 6"/></svg>
</div>

<!-- features -->
<div class="abs feat-pic" role="img" aria-label="Photo of a developer working on a laptop in front of skill bars for software development, engineering, expertise and outsourcing"></div>
<div class="abs feat-base"></div>
<div class="abs feat" style="top:2110px">
  <h2>OUR FEATURES</h2>
  <p style="margin-top:14px">Temporibus autem quibusdam et aut officiis debitis is aut rerum necessitatibus saepes eveniet ut etes seo lage voluptates repudiandae sint et molestiae non mes for Creating futures through building pres preservation.</p>
  <h4 style="margin-top:24px">Our Mission</h4>
  <p style="margin-top:6px">Voluptates repudiandae sint et molestiae non mes for Creating futures through building pres preservation.</p>
  <h4 style="margin-top:22px">Our Vision</h4>
  <p style="margin-top:6px">Voluptates repudiandae sint et molestiae non mes for Creating futures through building pres preservation.</p>
  <h4 style="margin-top:22px">Our Strategy</h4>
  <p style="margin-top:6px">Voluptates repudiandae sint et molestiae non mes for Creating futures through building pres preservation.</p>
</div>

<!-- contact -->
<section class="abs contact" role="img" aria-label="Photo of an office workspace with a warm gold overlay"></section>
<h2 class="abs contact-title">CONTACT US</h2>
<p class="abs contact-text">Temporibus autem quibusdam et aut officiis debitis is aut rerum necessitatibus saepes eveniet ut etes seo lage voluptates repudiandae sint et molestiae non mes for Creating futures through building pres preservation.</p>
<div class="abs field" style="top:2886px;height:46px">Name</div>
<div class="abs field" style="top:2946px;height:46px">Email Address</div>
<div class="abs field" style="top:3005px;height:97px">How can we help you?</div>
<div class="abs btn-submit">SUBMIT NOW</div>
<svg class="abs notch" style="top:3270px" viewBox="0 0 120 62"><path d="M0 0 H120 C85 2 64 20 60 62 C56 20 35 2 0 0Z" fill="#4a4536"/></svg>

<!-- footer -->
<div class="abs foot-brand"><i></i>Brightfold Systems</div>
<div class="abs social"><span></span><span></span><span></span><span></span><span></span></div>
<div class="abs foot-rule"></div>
<p class="abs copyright">Copyrights @ 2019 Brightfold Systems. All Rights Reserved.</p>

</body>
</html>
```